Poster for Office

Looking for an edgy, beautiful poster to hang up in my office that uses the quotes located below and potentially the image attached.

Title: Hadley's Maxims

Must have the following quotes included (punctuation and capitalization are flexible, do what you think looks the best they also don't need the quotation symbols):

"Don't order fish at a steakhouse"
"Be bold. The more you tell, the more you sell"
"admit nothing, deny everything, launch counterattack."
"avoid obviousness"
"never do anything until you're ready to do it"
"look good=feel good"
"always keep the advantage"
"never complain, never explain"
"Lay low, play dumb, keep moving"

Quotes

• Title: Hadley's Maxims

"avoid obviousness"
"look good=feel good"

```html
<!DOCTYPE html>
<html lang="en">
<head>
<meta charset="utf-8">
<title>Hadley's Maxims</title>
<link rel="stylesheet" href="https://fonts.googleapis.com/css2?family=Saira+Condensed:wght@700;800&display=swap">
<style>
  :root {
    --sky-light: #f4f5f6;
    --sky-mid: #b9bcbf;
    --sky-dark: #6f7276;
    --figure-light: #c9c9c9;
    --figure-dark: #5a5a5a;
    --blue-title: #2f5cf2;
    --blue-royal: #2350e4;
    --blue-soft: #4f7fda;
    --blue-deep: #1a1fc4;
    --blue-sky: #6db0ef;
    --blue-medium: #3462e2;
    --blue-slate: #5c80dc;
    --blue-cyan: #46b2ef;
    --blue-bright: #3d70ea;
    --blue-ink: #1b22de;
  }
  html, body {
    margin: 0;
    padding: 0;
    width: 1200px;
    height: 1200px;
    overflow: hidden;
    background: var(--sky-mid);
  }
  .poster {
    display: block;
    width: 1200px;
    height: 1200px;
  }
  .maxim {
    font-family: "Saira Condensed", "Arial Narrow", sans-serif;
    font-weight: 700;
  }
  .poster-title {
    font-family: "Saira Condensed", "Arial Narrow", sans-serif;
    font-weight: 800;
    fill: var(--blue-title);
  }
  .maxim--steakhouse { fill: var(--blue-royal); }
  .maxim--bold { fill: var(--blue-soft); }
  .maxim--admit { fill: var(--blue-deep); }
  .maxim--obvious { fill: var(--blue-sky); }
  .maxim--ready { fill: var(--blue-medium); }
  .maxim--look { fill: var(--blue-slate); }
  .maxim--advantage { fill: var(--blue-cyan); }
  .maxim--complain { fill: var(--blue-bright); }
  .maxim--lowdumb { fill: var(--blue-ink); }
</style>
</head>
<body>
<svg class="poster" viewBox="0 0 1200 1200" xmlns="http://www.w3.org/2000/svg">
  <defs>
    <radialGradient id="sky-glow" cx="600" cy="820" r="820" gradientUnits="userSpaceOnUse">
      <stop offset="0" stop-color="var(--sky-light)"/>
      <stop offset="0.35" stop-color="var(--sky-mid)"/>
      <stop offset="1" stop-color="var(--sky-dark)"/>
    </radialGradient>
    <linearGradient id="figure-tone" x1="0" y1="0" x2="1" y2="1">
      <stop offset="0" stop-color="var(--figure-dark)"/>
      <stop offset="1" stop-color="var(--figure-light)"/>
    </linearGradient>
  </defs>

  <rect class="backdrop" role="img" aria-label="Black and white photograph of a cloudy sky over a bright, glittering lake" x="0" y="0" width="1200" height="1200" fill="url(#sky-glow)"/>

  <g class="portrait-collage">
    <path role="img" aria-label="Photograph of a man's head and shoulder seen from behind, upper left" d="M0 0 H90 V340 Q40 330 0 360 Z" fill="url(#figure-tone)" opacity="0.85"/>
    <path role="img" aria-label="Photograph of a smiling man, left edge" d="M0 380 H130 Q140 530 110 690 H0 Z" fill="url(#figure-tone)" opacity="0.8"/>
    <path role="img" aria-label="Photograph of a man's head and shoulder in profile, upper right" d="M940 0 H1200 V520 Q1120 470 1080 330 Q1000 260 940 180 Z" fill="url(#figure-tone)" opacity="0.85"/>
    <path role="img" aria-label="Photograph of a smiling man, right edge" d="M1200 390 V675 Q1150 640 1140 540 Q1150 420 1200 390 Z" fill="url(#figure-tone)" opacity="0.8"/>
  </g>

  <g class="maxims-block">
    <text class="poster-title" x="140" y="304" font-size="134" textLength="927" lengthAdjust="spacingAndGlyphs">Hadley's Maxims</text>

    <text class="maxim maxim--steakhouse" x="157" y="464" font-size="64" textLength="906" lengthAdjust="spacingAndGlyphs">Don’t order fish at a steakhouse</text>
    <text class="maxim maxim--bold" x="149" y="537" font-size="42" textLength="924" lengthAdjust="spacingAndGlyphs">Be bold. The more you tell, the more you sell</text>
    <text class="maxim maxim--admit" x="147" y="600" font-size="36" textLength="916" lengthAdjust="spacingAndGlyphs">admit nothing, deny everything, launch counterattack</text>
    <text class="maxim maxim--obvious" x="147" y="707" font-size="98" textLength="920" lengthAdjust="spacingAndGlyphs">avoid obviousness</text>
    <text class="maxim maxim--ready" x="147" y="773" font-size="46" textLength="926" lengthAdjust="spacingAndGlyphs">never do anything until you’re ready to do it</text>
    <text class="maxim maxim--look" x="144" y="880" font-size="84" textLength="923" lengthAdjust="spacingAndGlyphs">look good=feel good</text>
    <text class="maxim maxim--advantage" x="140" y="940" font-size="54" textLength="927" lengthAdjust="spacingAndGlyphs">always keep the advantage</text>
    <text class="maxim maxim--complain" x="140" y="1013" font-size="66" textLength="927" lengthAdjust="spacingAndGlyphs">never complain, never explain</text>
    <text class="maxim maxim--lowdumb" x="144" y="1083" font-size="50" textLength="929" lengthAdjust="spacingAndGlyphs">lay low, play dumb, keep moving</text>
  </g>
</svg>
</body>
</html>
```